Wine bottle label for family vineyard

Label front and back for our background vineyard. BeLow is a label we used in the past. The gazebo is at the top of the vineyard. We want the front label to have the info we have currently with name etc. But we are open to fun on the back. Maybe a Covid mask would be appropriate Would like one with and one without. But I want the designer to feel free and go out of the box. Especially on back label.

Target Market(s)

None. It’s just for personal consumption We drink what we can and give the rest away.

Industry/Entity Type

Wine

Requirements
Must have
• Name our evening pour. Dunstrom family vineyard. Pinot noir. Year. Name of winemaker.
Nice to have
• The back label being fun is a plus. Maybe some quotes about wine and friends

```html
<!DOCTYPE html>
<html lang="en">
<head>
<meta charset="utf-8">
<title>our evening pour – Wine Labels</title>
<link rel="stylesheet" href="https://fonts.googleapis.com/css2?family=Chewy&family=Kaushan+Script&family=Oswald:wght@600;700&display=swap">
<style>
  :root {
    --label-green: #92f531;
    --frame-tan: #d99a4e;
    --brand-red: #d10a0a;
    --ink: #111111;
    --band-dark: #243030;
    --paper: #ffffff;
    --photo-light: #e4e4e4;
    --photo-mid: #9a9a9a;
    --photo-dark: #3a3a3a;
  }
  html, body {
    margin: 0;
    padding: 0;
    width: 1200px;
    height: 1110px;
    overflow: hidden;
    background: var(--paper);
  }
  .label-sheet { display: block; width: 1200px; height: 1110px; }
  .label-frame { stroke: var(--frame-tan); stroke-width: 16; }
  .back-label .label-frame { fill: var(--label-green); }
  .front-label .label-frame { fill: none; }
  .script-line { font-family: "Kaushan Script", cursive; fill: var(--ink); text-anchor: middle; }
  .toast-line { font-family: "Kaushan Script", cursive; fill: var(--brand-red); text-anchor: middle; }
  .wine-name { font-family: "Chewy", cursive; fill: var(--brand-red); text-anchor: middle; }
  .vineyard-line { font-family: "Chewy", cursive; fill: var(--ink); text-anchor: middle; }
  .brand-mark { font-family: "Chewy", cursive; fill: var(--brand-red); text-anchor: start; }
  .brand-dot { fill: var(--brand-red); }
  .varietal { font-family: "Oswald", sans-serif; font-weight: 700; fill: var(--paper); text-anchor: middle; }
  .origin { font-family: "Oswald", sans-serif; font-weight: 600; fill: var(--paper); text-anchor: middle; }
  .grape-art { fill: var(--frame-tan); opacity: 0.35; }
  .info-band { fill: var(--band-dark); }
</style>
</head>
<body>
<svg class="label-sheet" viewBox="0 0 1752 1620" xmlns="http://www.w3.org/2000/svg">
  <defs>
    <path id="label-shape" d="M68 128 Q420 -30 772 128 Q770 210 838 215 L838 1360 Q770 1365 772 1445 Q420 1640 68 1445 Q70 1365 6 1360 L6 215 Q70 210 68 128 Z"/>
    <clipPath id="front-clip">
      <use href="#label-shape" transform="translate(905 14)"/>
    </clipPath>
    <linearGradient id="photo-tone" x1="0" y1="0" x2="0" y2="1">
      <stop offset="0" stop-color="var(--photo-dark)"/>
      <stop offset="0.35" stop-color="var(--photo-mid)"/>
      <stop offset="0.7" stop-color="var(--photo-light)"/>
      <stop offset="1" stop-color="var(--photo-mid)"/>
    </linearGradient>
  </defs>

  <g class="back-label">
    <use class="label-frame" href="#label-shape"/>
    <text class="script-line" x="400" y="205" font-size="78">This vintage of</text>
    <text class="wine-name" x="405" y="350" font-size="100" textLength="545" lengthAdjust="spacingAndGlyphs">our evening pour</text>
    <text class="vineyard-line" x="408" y="412" font-size="46" textLength="555" lengthAdjust="spacingAndGlyphs">A Dunstrom Family Vineyard</text>
    <text class="script-line" x="435" y="575" font-size="80">is dedicated to:</text>
    <rect class="grape-art" x="160" y="625" width="500" height="480" rx="60" role="img" aria-label="Illustration of a grape cluster hanging from a vine with leaves"/>
    <text class="script-line" x="422" y="1170" font-size="40">Wine tastes best shared with friends.</text>
    <text class="toast-line" x="422" y="1225" font-size="38">Pour. Sip. Mask up. Repeat.</text>
    <circle class="brand-dot" cx="305" cy="1345" r="14"/>
    <text class="brand-mark" x="332" y="1365" font-size="62">Dunstrom</text>
  </g>

  <g class="front-label">
    <g clip-path="url(#front-clip)">
      <rect x="905" y="0" width="850" height="1620" fill="url(#photo-tone)" role="img" aria-label="Black and white photo of the gazebo at the top of the vineyard among trees and flowering plants"/>
      <path class="info-band" d="M905 1180 Q1330 1420 1752 1165 L1752 1640 L905 1640 Z"/>
    </g>
    <use class="label-frame" href="#label-shape" transform="translate(905 14)"/>
    <text class="wine-name" x="1332" y="838" font-size="112" textLength="655" lengthAdjust="spacingAndGlyphs">our evening pour</text>
    <text class="vineyard-line" x="1337" y="915" font-size="52" textLength="665" lengthAdjust="spacingAndGlyphs">A Dunstrom Family Vineyard</text>
    <circle class="brand-dot" cx="1205" cy="1090" r="14"/>
    <text class="brand-mark" x="1232" y="1110" font-size="62">Dunstrom</text>
    <text class="varietal" x="1340" y="1390" font-size="64">PINOT NOIR</text>
    <text class="origin" x="1328" y="1440" font-size="38">Sonoma Border</text>
    <text class="origin" x="1335" y="1482" font-size="38" xml:space="preserve">Novato  Marin County 2016</text>
    <text class="origin" x="1335" y="1524" font-size="30">Winemaker Pieter Dunstrom</text>
  </g>
</svg>
</body>
</html>
```